Business Card Design needed for logo design project

We need a business card design for a construction parts business.

We would like our main company logo on the front of the card and have our other company website logo on the rear of the card.

Both logos will be attached.

Front of card
Logo is KRV
Can we also have the wording "Construction Equipment Parts Specialists"
Main details to include:

Address:
Telephone:
Mobile:
Email:
Website:

Rear of card.

Logo is gearlodgehub.com.au (we would like this logo taking up the most of the rear)
Also we want under gearlodgehub.com.au the following wording "Parts Sourced For You From Across The Globe"
Updates

Please see new update for our design

Target Market(s)

Construction Industry.
Earthmoving Equipment owners.

Industry/Entity Type

Construction

Font styles to use
Sans Serif

Requirements
Must have
• Easy to read.
Clean and smart.
Should not have
• Should not have any colours other than the colours of our logos.

```html
<!DOCTYPE html>
<html lang="en">
<head>
<meta charset="utf-8">
<title>KRV Business Card – Front</title>
<link href="https://fonts.googleapis.com/css2?family=Carlito:wght@400;700&display=swap" rel="stylesheet">
<style>
  :root {
    --bg-core: #2e2e2e;
    --bg-edge: #0d0d0d;
    --brand-slate: #3b4d60;
    --brand-teal: #2a8fae;
    --stripe-blue: #17a5d8;
    --text-light: #f2f2f2;
  }
  html, body {
    margin: 0;
    padding: 0;
    overflow: hidden;
    background: #111;
  }
  .card {
    position: relative;
    width: 1200px;
    height: 722px;
    overflow: hidden;
    font-family: "Carlito", "Calibri", sans-serif;
    color: var(--text-light);
    background:
      repeating-linear-gradient(90deg, rgba(255,255,255,0.025) 0 1px, transparent 1px 5px),
      repeating-linear-gradient(0deg, rgba(0,0,0,0.08) 0 1px, transparent 1px 7px),
      radial-gradient(ellipse at 55% 35%, var(--bg-core) 0%, #1e1e1e 55%, var(--bg-edge) 100%);
  }
  .brand {
    position: absolute;
    left: 108px;
    top: 104px;
    display: flex;
    align-items: center;
    gap: 14px;
  }
  .brand-name {
    font-weight: 700;
    font-size: 150px;
    line-height: 1;
    letter-spacing: 2px;
    color: var(--brand-slate);
  }
  .brand-dot {
    width: 86px;
    height: 86px;
    border-radius: 50%;
    background: var(--brand-teal);
  }
  .tagline {
    position: absolute;
    left: 88px;
    top: 244px;
    margin: 0;
    font-weight: 400;
    font-size: 31px;
    line-height: 36px;
  }
  .contact {
    position: absolute;
    left: 588px;
    top: 238px;
    margin: 0;
    display: grid;
    grid-template-columns: 182px auto;
    font-size: 31px;
    line-height: 36px;
  }
  .contact dt, .contact dd { margin: 0; }
  .hazard-band {
    position: absolute;
    left: 0;
    top: 443px;
    width: 1200px;
    height: 142px;
  }
  .hazard-band polygon { fill: var(--stripe-blue); }
</style>
</head>
<body>
<div class="card">
  <div class="brand">
    <span class="brand-name">KRV</span>
    <span class="brand-dot"></span>
  </div>
  <p class="tagline">Construction Equipment<br>Parts Specialists</p>

  <dl class="contact">
    <dt>Address:</dt><dd>gearlodgehub.com.au</dd>
    <dt>Telephone:</dt><dd>123-456-789</dd>
    <dt>Mobile:</dt><dd>123-456-789</dd>
    <dt>Email:</dt><dd>gearlodgehub.com.au</dd>
    <dt>Website:</dt><dd>gearlodgehub.com.au</dd>
  </dl>

  <svg class="hazard-band" viewBox="0 0 1200 142" aria-hidden="true">
    <polygon points="-181,0 -101,0 16,142 -64,142"/>
    <polygon points="-64,0 16,0 133,142 53,142"/>
    <polygon points="53,0 133,0 250,142 170,142"/>
    <polygon points="170,0 250,0 367,142 287,142"/>
    <polygon points="287,0 367,0 484,142 404,142"/>
    <polygon points="404,0 484,0 601,142 521,142"/>
    <polygon points="521,0 601,0 718,142 638,142"/>
    <polygon points="638,0 718,0 835,142 755,142"/>
    <polygon points="755,0 835,0 952,142 872,142"/>
    <polygon points="872,0 952,0 1069,142 989,142"/>
    <polygon points="989,0 1069,0 1186,142 1106,142"/>
    <polygon points="1106,0 1186,0 1303,142 1223,142"/>
  </svg>
</div>
</body>
</html>
```